Ferris Contracting LLC Business Card Design

I am looking for a creative and unique business card design. We are a commercial construction general contractor. With the name "FERRIS" Contracting, I am hoping to see some neat designs that correlate with the name.

```html
<!DOCTYPE html>
<html lang="en">
<head>
<meta charset="utf-8">
<title>Ferris Contracting LLC – Business Card</title>
<link href="https://fonts.googleapis.com/css2?family=Exo+2:wght@400;700;800&display=swap" rel="stylesheet">
<style>
  :root {
    --backdrop: #dedede;
    --card-dark: #262626;
    --card-light: #ffffff;
    --brand-blue: #2a8fd0;
    --ink: #222222;
    --muted: #8a8a8a;
    --faint-grey: #f1f1f1;
    --faint-blue: #cfe5f4;
  }
  html, body {
    margin: 0;
    width: 1200px;
    height: 1000px;
    overflow: hidden;
    background: var(--backdrop);
    font-family: "Exo 2", sans-serif;
  }
  .card {
    position: absolute;
    left: 329px;
    width: 543px;
    height: 313px;
    overflow: hidden;
  }
  .card--front {
    top: 148px;
    background: var(--card-dark);
    display: flex;
    align-items: center;
    justify-content: center;
  }
  .card--back {
    top: 514px;
    background: var(--card-light);
  }
  .wordmark {
    color: var(--brand-blue);
    font-weight: 800;
    text-align: center;
    line-height: 1;
  }
  .wordmark__name {
    display: block;
    font-size: 62px;
    letter-spacing: 2px;
  }
  .wordmark__sub {
    display: block;
    font-size: 14px;
    letter-spacing: 7px;
    margin-top: 4px;
  }
  .card--back .wordmark {
    position: absolute;
    left: 36px;
    top: 42px;
    text-align: left;
  }
  .card--back .wordmark__name { font-size: 26px; letter-spacing: 1px; }
  .card--back .wordmark__sub { font-size: 6.5px; letter-spacing: 3.2px; margin-top: 2px; }
  .decor {
    position: absolute;
    right: -150px;
    bottom: -170px;
  }
  .person {
    position: absolute;
    left: 36px;
    top: 142px;
  }
  .person__name {
    margin: 0;
    color: var(--brand-blue);
    font-weight: 800;
    font-size: 20px;
    line-height: 1.1;
  }
  .person__title {
    margin: 0;
    color: var(--muted);
    font-size: 18px;
    line-height: 1.1;
  }
  .contacts {
    position: absolute;
    left: 36px;
    top: 206px;
    margin: 0;
    padding: 0;
    list-style: none;
  }
  .contacts li {
    display: flex;
    align-items: center;
    height: 25.5px;
    font-size: 18px;
    color: var(--ink);
  }
  .contacts svg {
    width: 12px;
    height: 12px;
    margin-right: 10px;
    fill: var(--brand-blue);
  }
</style>
</head>
<body>
  <section class="card card--front">
    <div class="wordmark">
      <span class="wordmark__name">FERRIS</span>
      <span class="wordmark__sub">CONTRACTING</span>
    </div>
  </section>

  <section class="card card--back">
    <svg class="decor" width="420" height="420" viewBox="0 0 420 420" aria-hidden="true">
      <circle cx="210" cy="210" r="210" fill="var(--faint-grey)"/>
    </svg>

    <div class="wordmark">
      <span class="wordmark__name">FERRIS</span>
      <span class="wordmark__sub">CONTRACTING</span>
    </div>

    <div class="person">
      <p class="person__name">NAME SURNAME</p>
      <p class="person__title">TITLE</p>
    </div>

    <ul class="contacts">
      <li>
        <svg viewBox="0 0 24 24"><path d="M6.6 10.8a15.1 15.1 0 0 0 6.6 6.6l2.2-2.2a1 1 0 0 1 1-.25 11.4 11.4 0 0 0 3.6.57 1 1 0 0 1 1 1V20a1 1 0 0 1-1 1A17 17 0 0 1 3 4a1 1 0 0 1 1-1h3.5a1 1 0 0 1 1 1c0 1.25.2 2.45.57 3.57a1 1 0 0 1-.25 1z"/></svg>
        (123) 456-7890
      </li>
      <li>
        <svg viewBox="0 0 24 24"><path d="M2 5h20v14H2z M3.5 6.5 12 13l8.5-6.5" fill="none" stroke="var(--brand-blue)" stroke-width="2.5"/></svg>
        name@website.com
      </li>
      <li>
        <svg viewBox="0 0 24 24"><path d="M12 2a7 7 0 0 0-7 7c0 5.2 7 13 7 13s7-7.8 7-13a7 7 0 0 0-7-7zm0 9.5A2.5 2.5 0 1 1 12 6.5a2.5 2.5 0 0 1 0 5z"/></svg>
        website.com
      </li>
    </ul>
  </section>
</body>
</html>
```